Cornflute Firewood advertising Sign for passing by traffic

900mm W
1200mm H

I am looking for a design to place outside of our nursery to advertise our firewood. We have a lot of traffic passing by and want to capture the eyes of potential customers.

We want a modern sleek look that will set the tone for the product

key things i want to hit -
Visual of firewood or fire
Quality product
we deliver
Clean firewood

Target Market(s)

Older retired people
Young families
Passing traffic

Industry/Entity Type

Firewood

Font styles to use
Serif
Sans Serif

Requirements
Must have
• Great eye catching picture
• colorful
• Easy to read for passers by
• Picture of firewood or fireplace or anything you seem relevant to the sale of firewood
• If using picture of firewood make sure it is Australian hardwood
Should not have
• Phone number or business name

```html
<!DOCTYPE html>
<html lang="en">
<head>
<meta charset="UTF-8">
<title>Clean Firewood Sign</title>
<link rel="stylesheet" href="https://fonts.googleapis.com/css2?family=Anton&display=swap">
<style>
  :root {
    --ember-hot: #f29a3a;
    --ember-mid: #c8501c;
    --ember-deep: #6a1a08;
    --char: #1a0a06;
    --navy-ink: #0d1220;
    --amber: #f7a33a;
    --rule-red: #b4322a;
  }
  * { margin: 0; padding: 0; box-sizing: border-box; }
  html, body { width: 904px; height: 1200px; overflow: hidden; background: var(--char); }
  .sign {
    position: relative;
    width: 904px;
    height: 1200px;
    overflow: hidden;
    font-family: "Anton", "Oswald", sans-serif;
  }
  .fire-photo {
    position: absolute;
    inset: 0;
    background:
      radial-gradient(ellipse 45% 30% at 45% 35%, var(--ember-hot) 0%, var(--ember-mid) 45%, transparent 80%),
      radial-gradient(ellipse 30% 40% at 88% 40%, #ffd9a0 0%, var(--ember-hot) 30%, transparent 70%),
      radial-gradient(ellipse 40% 25% at 20% 12%, #e0802e 0%, transparent 70%),
      linear-gradient(180deg, var(--ember-deep) 0%, var(--ember-mid) 40%, var(--ember-deep) 70%, var(--char) 100%);
  }
  .message-panel {
    position: absolute;
    left: 17px;
    right: 12px;
    top: 638px;
    bottom: 18px;
    background: var(--navy-ink);
  }
  .headline {
    position: absolute;
    left: 0;
    width: 904px;
    text-align: center;
    color: var(--amber);
    font-size: 104px;
    line-height: 1;
    text-transform: uppercase;
    letter-spacing: 1px;
  }
  .headline--quality { top: 680px; }
  .headline--deliver { top: 868px; }
  .divider {
    position: absolute;
    left: 80px;
    width: 744px;
    height: 5px;
    background: var(--rule-red);
  }
  .divider--upper { top: 829px; }
  .divider--lower { top: 1002px; }
  .product-band {
    position: absolute;
    left: 9px;
    right: 4px;
    top: 1028px;
    height: 148px;
    background: var(--amber);
  }
  .product-band__text {
    position: absolute;
    left: 0;
    width: 904px;
    top: 1045px;
    text-align: center;
    color: var(--navy-ink);
    font-size: 104px;
    line-height: 1;
    text-transform: uppercase;
    letter-spacing: 1px;
  }
</style>
</head>
<body>
  <main class="sign">
    <div class="fire-photo" role="img" aria-label="Close-up photograph of glowing hardwood logs burning with orange flames"></div>
    <div class="message-panel"></div>
    <h1 class="headline headline--quality">Quality Product</h1>
    <div class="divider divider--upper"></div>
    <h2 class="headline headline--deliver">We Deliver</h2>
    <div class="divider divider--lower"></div>
    <div class="product-band"></div>
    <p class="product-band__text">Clean Firewood</p>
  </main>
</body>
</html>
```